Business Card Tech Company
Veradon Corp
Project: Business Card Tech Company
Business Card Tech Company -
Creative Brief
Simple
Marcel Dufresne
CEO
2745 Rue Belcourt, Québec, QC G2K 3P7, Canada
mdufresne@veradoncorp-example.com
www.veradoncorp-example.com
You can add Twitter @veradoncorp We are very open to different designs, We will provide fast feedback, You can try many styles and many fonts, Right now, our slogan is: ideas brought closer. You can put it on some designs if it fits well, consider we might want to change it.
We would like a back mostly visual, without much info.

```html
<!DOCTYPE html>
<html lang="en">
<head>
<meta charset="utf-8">
<title>Veradon Corp — Business Card</title>
<link rel="stylesheet" href="https://fonts.googleapis.com/css2?family=Ubuntu:wght@400;500&family=Open+Sans:wght@400;600&display=swap">
<style>
  :root {
    --bg: #ecebe8;
    --card: #ffffff;
    --brand-blue: #2f86c6;
    --brand-grey: #6d6e71;
    --text-grey: #7a7b7e;
    --rule: #e3e4e6;
    --shadow: rgba(0, 0, 0, 0.16);
  }
  * { box-sizing: border-box; margin: 0; padding: 0; }
  html, body { width: 1200px; height: 794px; overflow: hidden; }
  body {
    background: var(--bg);
    font-family: "Open Sans", Arial, sans-serif;
    display: flex;
    align-items: center;
    justify-content: center;
    gap: 60px;
  }
  .card {
    width: 520px;
    height: 297px;
    background: var(--card);
    box-shadow: 0 6px 18px var(--shadow);
    position: relative;
  }
  .brand {
    display: flex;
    align-items: center;
    gap: 14px;
    font-family: "Ubuntu", sans-serif;
    font-weight: 500;
    color: var(--brand-blue);
  }
  .brand-dot { border-radius: 50%; background: var(--brand-grey); flex: none; }

  /* front */
  .card-front .brand { position: absolute; left: 40px; top: 38px; font-size: 46px; }
  .card-front .brand-dot { width: 58px; height: 58px; }
  .tagline {
    position: absolute; left: 290px; top: 104px;
    font-family: "Ubuntu", sans-serif; font-size: 12px; color: var(--text-grey);
  }
  .rule { position: absolute; left: 0; right: 0; top: 150px; border-top: 1px solid var(--rule); }
  .person {
    position: absolute; right: 224px; top: 160px;
    font-family: "Ubuntu", sans-serif; font-size: 15px; font-weight: 500; color: var(--brand-blue);
  }
  .role {
    position: absolute; left: 306px; top: 162px;
    font-family: "Ubuntu", sans-serif; font-size: 13px; color: var(--text-grey);
  }
  .address {
    position: absolute; left: 40px; top: 212px;
    font-size: 10px; line-height: 1.5; color: var(--text-grey);
  }
  .contact {
    position: absolute; left: 306px; top: 188px;
    font-size: 10px; line-height: 1.6; color: var(--text-grey); list-style: none;
  }

  /* back */
  .card-back .brand {
    position: absolute; left: 0; right: 0; top: 90px;
    justify-content: center; font-size: 58px;
  }
  .card-back .brand-dot { width: 72px; height: 72px; }
  .handle {
    position: absolute; left: 0; right: 0; bottom: 30px;
    display: flex; justify-content: center; align-items: center; gap: 8px;
    font-size: 12px; color: var(--text-grey);
  }
  .handle-box { width: 16px; height: 16px; background: var(--brand-blue); border-radius: 2px; }
</style>
</head>
<body>
  <section class="card card-front">
    <div class="brand"><span class="brand-dot"></span>Veradon</div>
    <p class="tagline">ideas brought closer</p>
    <div class="rule"></div>
    <p class="person">Marcel Dufresne</p>
    <p class="role">CEO</p>
    <p class="address">2745 Rue Belcourt, Québec, QC<br>G2K 3P7<br>Canada</p>
    <ul class="contact">
      <li>C : 418 555 0172</li>
      <li>E : mdufresne@veradoncorp-example.com</li>
      <li>W : www.veradoncorp-example.com</li>
    </ul>
  </section>

  <section class="card card-back">
    <div class="brand"><span class="brand-dot"></span>Veradon</div>
    <p class="handle"><span class="handle-box"></span>@veradoncorp</p>
  </section>
</body>
</html>
```